Gospel Tract titled "A Clear Road Upward From Iowa."

This will be a bi-fold brochure. The design will be in the front panel of the brochure which is 4 inches wide and 8.5 inches high. This is a common brochure among Gospel tracts in the series, "A Clear Road Upward from ______________ ." The blank is usually a state, city, or other location. I want a "fun" image of Iowa or something representing Iowa at the bottom. A graphic representing "heaven" at the top. Perhaps a meandering road between the two. The words, "A Clear Road Upward from Iowa", but be on the front somewhere. I am also open to other designs with this theme and the words "A Clear Road Upward from Iowa." My suggestion is just one idea.

Target Market(s)

Non-Christians who are interested in knowing how to get to heaven

Requirements
Must have
• Something specific to the state of Iowa at the bottom: farms, state fair, cows, barns, power windmills, the capitol building, etc.
Nice to have
• I would like something bright, colorful, with a fun Iowa image at the bottom.
Should not have
• Religous symbolism....no doves, angels, crosses, etc.

```html
<!DOCTYPE html>
<html lang="en">
<head>
<meta charset="utf-8">
<title>A Clear Road Upward from Iowa</title>
<link rel="stylesheet" href="https://fonts.googleapis.com/css2?family=Bebas+Neue&family=Great+Vibes&display=swap">
<style>
  :root {
    --cream: #fdeed6;
    --sky-haze: #efe6d4;
    --sky-rose: #b8908a;
    --sky-glow: #f4f2e6;
    --tan: #d2b49a;
    --gold: #f9c06a;
    --amber: #fbb24c;
    --ember: #e2440e;
    --umber: #6e2410;
    --rust: #a4552a;
    --script-red: #e0000f;
    --white: #ffffff;
    --dusk: #f6c98e;
    --park-green: #5f8a2c;
    --plaza: #d9b59a;
  }
  html, body {
    margin: 0;
    padding: 0;
    width: 1200px;
    height: 2548px;
    overflow: hidden;
    background: var(--cream);
  }
  .front-panel {
    position: relative;
    width: 1200px;
    height: 2548px;
    overflow: hidden;
    background: linear-gradient(180deg, var(--sky-haze) 0%, var(--cream) 48%, #fde6c4 72%, var(--dusk) 80%);
  }
  .heaven-sky {
    position: absolute;
    left: 0;
    top: 0;
    width: 1200px;
    height: 1160px;
    background:
      radial-gradient(ellipse 260px 420px at 600px 300px, var(--sky-glow) 0%, rgba(244,242,230,0.7) 45%, rgba(244,242,230,0) 100%),
      radial-gradient(ellipse 500px 300px at 1050px 150px, var(--sky-rose) 0%, rgba(184,144,138,0) 100%),
      radial-gradient(ellipse 400px 260px at 120px 120px, #c7a79a 0%, rgba(199,167,154,0) 100%),
      linear-gradient(180deg, #d9c7b6 0%, #ede4d2 60%, rgba(253,238,214,0) 100%);
  }
  .iowa-skyline {
    position: absolute;
    left: 0;
    top: 1960px;
    width: 1200px;
    height: 588px;
    background:
      linear-gradient(180deg, rgba(246,201,142,0) 0%, #c9a489 14%, #8c7a5e 26%, var(--park-green) 48%, #7a8f3c 62%, var(--plaza) 80%, #c99e84 100%);
  }
  .title-art {
    position: absolute;
    left: 0;
    top: 0;
    width: 1200px;
    height: 2548px;
  }
  .title-lead {
    font-family: "Bebas Neue", sans-serif;
    fill: var(--tan);
  }
  .title-big {
    font-family: "Bebas Neue", sans-serif;
  }
  .title-from {
    font-family: "Great Vibes", cursive;
    fill: var(--script-red);
    stroke: var(--white);
    stroke-width: 16;
    stroke-linejoin: round;
    paint-order: stroke;
  }
</style>
</head>
<body>
<main class="front-panel">
  <div class="heaven-sky" role="img" aria-label="Glowing sky with bright clouds and light pouring down from above"></div>
  <div class="iowa-skyline" role="img" aria-label="Des Moines skyline at sunset seen from the state capitol plaza, with flags, gardens and a long street leading downtown"></div>

  <svg class="title-art" width="1200" height="2548" viewBox="0 0 1200 2548" aria-labelledby="tract-title">
    <title id="tract-title">A Clear Road Upward from Iowa</title>
    <defs>
      <linearGradient id="upward-fill" x1="0" y1="645" x2="0" y2="1045" gradientUnits="userSpaceOnUse">
        <stop offset="0" stop-color="var(--rust)"/>
        <stop offset="0.45" stop-color="var(--umber)"/>
        <stop offset="1" stop-color="#8a5a2a"/>
      </linearGradient>
      <linearGradient id="iowa-fill" x1="0" y1="1550" x2="0" y2="1970" gradientUnits="userSpaceOnUse">
        <stop offset="0" stop-color="var(--amber)"/>
        <stop offset="0.55" stop-color="var(--amber)"/>
        <stop offset="1" stop-color="var(--ember)"/>
      </linearGradient>
    </defs>

    <text class="title-lead" x="612" y="510" text-anchor="middle" font-size="142" textLength="300" lengthAdjust="spacingAndGlyphs">A CLEAR</text>
    <text class="title-lead" x="602" y="624" text-anchor="middle" font-size="142" textLength="250" lengthAdjust="spacingAndGlyphs">ROAD</text>

    <text class="title-big" x="275" y="1045" font-size="572" fill="url(#upward-fill)" textLength="665" lengthAdjust="spacingAndGlyphs">UPW</text>
    <text class="title-big" x="262" y="1490" font-size="578" fill="var(--gold)" textLength="660" lengthAdjust="spacingAndGlyphs">ARD</text>
    <text class="title-big" x="165" y="1970" font-size="600" fill="url(#iowa-fill)" textLength="885" lengthAdjust="spacingAndGlyphs">IOWA</text>

    <text class="title-from" x="300" y="1590" font-size="330" transform="rotate(-6 590 1520)" textLength="570" lengthAdjust="spacingAndGlyphs">from</text>
  </svg>
</main>
</body>
</html>
```